Hall of Fame announcement social media post

I need a social media Hall of Fame announcement designed in the styles of some of the examples I've posted. I have attached the two gentlemens head shots ... the names are Carl Whitby and Ron Fadley

It is for the TENNESSEE LINKS LEGENDS GALLERY also include 2025 Inductees ... I have also attached the logo... make the post in similar colors as the logo

```html
<!DOCTYPE html>
<html lang="en">
<head>
<meta charset="utf-8">
<title>Tennessee Links Legends Gallery – 2025 Inductees</title>
<link rel="stylesheet" href="https://fonts.googleapis.com/css2?family=Oswald:wght@700&family=Montserrat:ital,wght@0,800;1,900&family=Poppins:ital,wght@1,800&family=Playfair+Display:ital,wght@1,700&display=swap">
<style>
  :root {
    --navy: #1f3470;
    --navy-deep: #13244f;
    --red: #c4302b;
    --paper: #eceef1;
    --white: #ffffff;
  }
  * { margin: 0; padding: 0; box-sizing: border-box; }
  html, body { width: 1200px; height: 675px; overflow: hidden; background: var(--paper); }
  .post { position: relative; width: 1200px; height: 675px; overflow: hidden; background: var(--paper); }
  .backdrop { position: absolute; inset: 0; }

  .brand-name {
    position: absolute; left: 235px; top: 72px; width: 240px;
    text-align: center; color: var(--navy);
    font-family: "Montserrat", sans-serif; font-weight: 800; font-style: normal;
    font-size: 26px; line-height: 1.3;
  }

  .headline { position: absolute; left: 160px; top: 215px; width: 380px; height: 330px; overflow: visible; }
  .headline .kicker { font-family: "Montserrat", sans-serif; font-style: italic; font-weight: 900; fill: var(--navy); }
  .headline .big { font-family: "Oswald", sans-serif; font-weight: 700; fill: var(--navy); }

  .year {
    position: absolute; left: 190px; top: 532px; width: 300px; text-align: center;
    font-family: "Playfair Display", serif; font-style: italic; font-weight: 700;
    font-size: 36px; line-height: 1.1; color: var(--red);
  }

  .portrait {
    position: absolute; background: var(--white); padding: 4px;
    border-bottom-right-radius: 54px;
  }
  .portrait .photo { width: 100%; height: 100%; border-bottom-right-radius: 50px; }
  .portrait--whitby { left: 609px; top: 62px; width: 200px; height: 274px; }
  .portrait--whitby .photo { background: linear-gradient(160deg, #d7dde6 0%, #7c8aa6 55%, #1b1f2b 100%); }
  .portrait--fadley { left: 837px; top: 359px; width: 199px; height: 274px; }
  .portrait--fadley .photo { background: linear-gradient(170deg, #2a62c7 0%, #2f4f9b 55%, #16192a 100%); }

  .nameplate { position: absolute; height: 48px; }
  .nameplate .shadow { position: absolute; inset: 0; background: var(--red); }
  .nameplate .face {
    position: absolute; inset: 0; background: var(--navy); color: var(--white);
    font-family: "Poppins", sans-serif; font-style: italic; font-weight: 800;
    font-size: 27px; display: flex; align-items: center; justify-content: center;
  }
  .nameplate--whitby { left: 809px; top: 164px; width: 222px; }
  .nameplate--whitby .shadow { transform: translate(6px, 4px); }
  .nameplate--whitby .face { clip-path: polygon(0 0, 96% 0, 100% 100%, 0 100%); padding-left: 6px; }
  .nameplate--fadley { left: 627px; top: 466px; width: 210px; }
  .nameplate--fadley .shadow { transform: translate(-6px, 4px); }
  .nameplate--fadley .face { clip-path: polygon(4% 0, 100% 0, 100% 100%, 0 100%); }
</style>
</head>
<body>
<main class="post">
  <svg class="backdrop" width="1200" height="675" viewBox="0 0 1200 675">
    <defs>
      <linearGradient id="scene" x1="0" y1="0" x2="1" y2="1">
        <stop offset="0" stop-color="#e4e6ea"/>
        <stop offset="0.55" stop-color="#eef0f3"/>
        <stop offset="1" stop-color="#d9dce1"/>
      </linearGradient>
      <linearGradient id="edge" x1="0" y1="0" x2="0" y2="1">
        <stop offset="0" stop-color="#1a2d5e"/>
        <stop offset="1" stop-color="#13244f"/>
      </linearGradient>
    </defs>
    <rect width="1200" height="675" fill="url(#scene)" role="img" aria-label="Faded grayscale photo of a clubhouse building with trees and a walkway"/>
    <polygon points="0,0 109,0 53,675 0,675" fill="url(#edge)"/>
    <polygon points="1153,0 1200,0 1200,675 1100,675" fill="url(#edge)"/>
  </svg>

  <div class="brand-name">Tennessee Links<br>Legends<br>Gallery</div>

  <svg class="headline" viewBox="0 0 380 330">
    <g transform="skewX(-8)">
      <text class="kicker" x="55" y="38" font-size="32" textLength="345" lengthAdjust="spacingAndGlyphs">TENNESSEE LINKS</text>
      <text class="big" x="70" y="155" font-size="132" textLength="330" lengthAdjust="spacingAndGlyphs">LEGENDS</text>
      <text class="big" x="82" y="318" font-size="190" textLength="318" lengthAdjust="spacingAndGlyphs">GALLERY</text>
    </g>
  </svg>

  <div class="year">2025 Inductees</div>

  <figure class="portrait portrait--whitby">
    <div class="photo" role="img" aria-label="Headshot of Carl Whitby in a dark suit and light tie"></div>
  </figure>
  <div class="nameplate nameplate--whitby"><div class="shadow"></div><div class="face">Carl Whitby</div></div>

  <figure class="portrait portrait--fadley">
    <div class="photo" role="img" aria-label="Headshot of Ron Fadley in a dark suit and red tie against a blue backdrop"></div>
  </figure>
  <div class="nameplate nameplate--fadley"><div class="shadow"></div><div class="face">Ron Fadley</div></div>
</main>
</body>
</html>
```